Hello - we need a label design for our Quillon Health Hair Loss supplement. It is a natural hair loss supplement for black/african american women to regrow new hair and help restore hair loss & thinning hair due to vitamin deficiencies, traction alopecia, etc. It is a science based efficacious supplement with a centuries old medicinal herbal formula.
Attached is the logo & files of other generic competition and also Black hair products for your perusal. The label has to be a upscale and have an ethnic flair to it. The product is clinically effective, leveraged by Ancient Wisdom and Modern Science. The front of the label should include the following:
Quillon Health (logo)
Crown Revitalizer
Advanced Women’s Hair Loss Formula
TRACTION ALOPECIA THERAPY
- Prevents hair loss & restores thinning, fragile hair
- Promotes Natural Hair Growth
- Strengthens Hair for less breakage
- Visibly increases hair density & thickness
- Thicker, Stronger, Longer, Hydrated hair
- Promotes Follicle regeneration & Hair Growth
Site-Specific for hair loss & stunted growth
60 capsules 30-day supply
Target Market(s)
Black/African American Women
Look and feel

```html
<!DOCTYPE html>
<html lang="en">
<head>
<meta charset="utf-8">
<title>Quillon Health Crown Revitalizer – Label</title>
<link href="https://fonts.googleapis.com/css2?family=Montserrat:wght@700;800&family=Oswald:wght@500&family=Barlow+Semi+Condensed:wght@400;500;600;700&family=Barlow:wght@400;500;700&display=swap" rel="stylesheet">
<style>
  :root{
    --stage:#ffffff;
    --label:#0d0d0d;
    --label-band:#1b1b1b;
    --bronze:#c98a47;
    --bronze-dark:#8a5426;
    --bronze-light:#e0a866;
    --heading-bronze:#d98a3d;
    --text:#f2f2f2;
    --text-soft:#d9d9d9;
    --rule:#7a4f28;
  }
  *{box-sizing:border-box;margin:0;padding:0}
  html,body{width:1012px;height:1200px;overflow:hidden;background:var(--stage)}
  body{position:relative;font-family:"Barlow",sans-serif;color:var(--text)}

  .label{position:absolute;left:14px;top:395px;width:984px;height:410px;
    background:radial-gradient(ellipse at 50% 40%,#1c1c1c 0%,var(--label) 70%);overflow:hidden}
  .label__band{position:absolute;left:0;right:0;top:353px;height:40px;background:var(--label-band)}
  .label__stripe{position:absolute;left:0;bottom:0;width:100%;height:57px}

  /* left panel */
  .benefits{position:absolute;left:21px;top:24px;width:240px;list-style:none}
  .benefits__item{display:flex;align-items:center;gap:8px;height:23px;border-bottom:1px solid var(--rule);
    font:600 10.5px "Barlow Semi Condensed",sans-serif;color:var(--heading-bronze)}
  .benefits__item:last-child{border-bottom:0}
  .benefits__icon{width:20px;height:8px;flex:none}
  .story{position:absolute;left:21px;top:104px;width:240px;font:400 8.3px/11.2px "Barlow",sans-serif;color:var(--text-soft)}
  .story p+p{margin-top:11px}
  .checks{position:absolute;left:21px;top:277px;width:250px;list-style:none;
    font:700 8.6px/12.4px "Barlow",sans-serif;color:var(--text)}
  .checks li{position:relative;padding-left:12px}
  .checks li::before{content:"✓";position:absolute;left:0;color:var(--bronze)}

  /* front panel */
  .brand{position:absolute;left:322px;top:58px;width:340px;display:flex;justify-content:center;align-items:center;gap:8px;
    font:700 27px "Montserrat",sans-serif;color:var(--bronze-light)}
  .brand__dot{width:12px;height:12px;border-radius:50%;background:var(--bronze-light)}
  .title{position:absolute;left:322px;top:103px;width:340px;text-align:center;font-family:"Montserrat",sans-serif;font-weight:700;color:#fff;line-height:1}
  .title__line1{font-size:44px;letter-spacing:1px}
  .title__line2{font-size:37px;margin-top:7px}
  .formula{position:absolute;left:322px;top:198px;width:338px;height:36px;border-radius:8px;
    background:linear-gradient(180deg,var(--bronze-light),var(--bronze-dark));border:1px solid #e8b77c;
    display:flex;align-items:center;justify-content:center;font:500 17px "Oswald",sans-serif;letter-spacing:1.3px;color:#fff}
  .therapy{position:absolute;left:322px;top:245px;font:700 13.5px "Barlow Semi Condensed",sans-serif;color:#fff}
  .claims{position:absolute;left:322px;top:265px;list-style:none;font:400 8.8px/12.6px "Barlow Semi Condensed",sans-serif;color:var(--text-soft)}
  .claims li{display:flex;align-items:center;gap:5px}
  .claims svg{width:10px;height:5px}
  .portrait{position:absolute;left:535px;top:245px;width:124px;height:124px;border-radius:50%;
    background:radial-gradient(circle at 55% 45%,#f4f1ee 0%,#e6dcd4 55%,#3a2a22 100%);border:2px solid #fff}
  .count{position:absolute;left:323px;top:353px;width:80px;height:57px;border-radius:8px 8px 0 0;
    background:var(--label);border:2px solid var(--bronze);border-bottom:0;text-align:center}
  .count__num{font:800 30px/1 "Montserrat",sans-serif;color:#fff;margin-top:6px;-webkit-text-stroke:1px var(--bronze)}
  .count__unit{font:500 8px "Oswald",sans-serif;letter-spacing:1px;color:var(--bronze-light)}
  .supply{position:absolute;left:412px;top:360px;color:#fff}
  .supply__days{font:700 12.5px "Barlow Semi Condensed",sans-serif}
  .supply__note{font:500 11px "Barlow Semi Condensed",sans-serif}

  /* right panel */
  .directions{position:absolute;left:720px;top:31px;width:250px;font:400 8.3px/11.2px "Barlow",sans-serif;color:var(--text)}
  .directions h3{font:700 8.3px "Barlow",sans-serif;color:var(--heading-bronze)}
  .directions p+p{margin-top:11px}
  .disclaimer{position:absolute;left:720px;top:125px;width:242px;height:56px;border:1px solid var(--bronze);
    padding:9px 13px;font:400 8px/11px "Barlow",sans-serif;color:var(--text)}
  .maker{position:absolute;left:722px;top:201px;width:242px;height:82px;border:1px solid var(--bronze);text-align:center}
  .maker__head{background:linear-gradient(180deg,var(--bronze),var(--bronze-dark));font:600 10px/13px "Barlow",sans-serif;color:#fff;padding:1px 0}
  .maker__body{font:400 10.8px/14px "Barlow Semi Condensed",sans-serif;color:#fff;padding-top:4px}
  .ingredients{position:absolute;left:724px;top:302px;width:240px;font:400 8.3px/11.2px "Barlow",sans-serif;color:var(--text)}
  .ingredients b{color:var(--heading-bronze);font-weight:700}
</style>
</head>
<body>
<section class="label" aria-label="Quillon Health Crown Revitalizer bottle label">
  <div class="label__band"></div>
  <svg class="label__stripe" viewBox="0 0 984 57" preserveAspectRatio="none" aria-hidden="true">
    <defs><linearGradient id="bronzeBand" x1="0" y1="0" x2="0" y2="1">
      <stop offset="0" stop-color="#e0a866"/><stop offset="1" stop-color="#8a5426"/></linearGradient></defs>
    <path d="M0 47 H612 L632 38 H984 V57 H0 Z" fill="url(#bronzeBand)"/>
    <path d="M402 47 H612 L632 38 H984" fill="none" stroke="#0d0d0d" stroke-width="1.5"/>
  </svg>

  <ul class="benefits">
    <li class="benefits__item"><svg class="benefits__icon" viewBox="0 0 20 8"><path d="M1 6 Q5 0 10 4 T19 2" fill="none" stroke="#aaa" stroke-width="1.5"/></svg>Fight Hair Loss and Thinning Hair</li>
    <li class="benefits__item"><svg class="benefits__icon" viewBox="0 0 20 8"><path d="M1 6 Q5 0 10 4 T19 2" fill="none" stroke="#aaa" stroke-width="1.5"/></svg>Traction Alopecia Therapy</li>
    <li class="benefits__item"><svg class="benefits__icon" viewBox="0 0 20 8"><path d="M1 6 Q5 0 10 4 T19 2" fill="none" stroke="#aaa" stroke-width="1.5"/></svg>Site-Specific for Hair Loss &amp; Stunted Growth</li>
  </ul>
  <div class="story">
    <p>Quillon Health hair regrowth formulas provide intensive nourishment for receding hairlines, breakage around the hairline, excessively thinning hair, Traction Alopecia, and poor hair density.†</p>
    <p>Our Advanced Women’s Formula is specifically created for women’s unique needs with a revolutionary combination of Traditional Chinese Medicine integrated with modern science to create the latest breakthrough in achieving full, lustrous, healthy hair. By combining a powerful mixture of standardized herbs such as He Shou Wu and Horse Chestnut Extract, with vital hair energizing co-factor nutrients such as Silica, Biotin, and more, QH’s Advanced Women’s Formula helps you maximize your hair’s potential naturally.†</p>
  </div>
  <ul class="checks">
    <li>Accelerate Visibly Thicker-Looking, Stronger-Feeling, Healthier hair</li>
    <li>Natural, Vegan &amp; 100% Drug Free</li>
    <li>Clinically Effective Ingredients</li>
    <li>Modern Science * Ancient Wisdom</li>
  </ul>

  <div class="brand"><span class="brand__dot"></span>Quillon Health</div>
  <h1 class="title"><div class="title__line1">CROWN</div><div class="title__line2">REVITALIZER</div></h1>
  <div class="formula">ADVANCED WOMEN’S HAIR LOSS FORMULA</div>
  <h2 class="therapy">TRACTION ALOPECIA THERAPY</h2>
  <ul class="claims">
    <li><svg viewBox="0 0 10 5"><path d="M0 4 Q3 0 5 2.5 T10 1" fill="none" stroke="#999" stroke-width="1"/></svg>Prevents hair loss &amp; restores thinning, fragile hair</li>
    <li><svg viewBox="0 0 10 5"><path d="M0 4 Q3 0 5 2.5 T10 1" fill="none" stroke="#999" stroke-width="1"/></svg>Promotes Natural Hair Growth</li>
    <li><svg viewBox="0 0 10 5"><path d="M0 4 Q3 0 5 2.5 T10 1" fill="none" stroke="#999" stroke-width="1"/></svg>Strengthens Hair for less breakage</li>
    <li><svg viewBox="0 0 10 5"><path d="M0 4 Q3 0 5 2.5 T10 1" fill="none" stroke="#999" stroke-width="1"/></svg>Visibly increases hair density &amp; thickness</li>
    <li><svg viewBox="0 0 10 5"><path d="M0 4 Q3 0 5 2.5 T10 1" fill="none" stroke="#999" stroke-width="1"/></svg>Thicker, Stronger, Longer, Hydrated hair</li>
    <li><svg viewBox="0 0 10 5"><path d="M0 4 Q3 0 5 2.5 T10 1" fill="none" stroke="#999" stroke-width="1"/></svg>Promotes Follicle regeneration &amp; Hair Growth</li>
  </ul>
  <div class="portrait" role="img" aria-label="Circular portrait photo of a smiling woman with long dark hair"></div>
  <div class="count"><div class="count__num">60</div><div class="count__unit">CAPSULES</div></div>
  <div class="supply"><div class="supply__days">30-DAY SUPPLY</div><div class="supply__note">Site-Specific for hair loss &amp; stunted growth</div></div>

  <div class="directions">
    <h3>DIRECTIONS FOR USE:</h3>
    <p>Take 1 tablet, two times daily, with a meal. Do not exceed recommended intake. Best when taken in the morning upon awakening and prior to bedtime.</p>
    <p>FOR BEST RESULTS, THIS PRODUCT SHOULD BE TAKEN FOR A MINIMUM OF 3-4 MONTHS. INDIVIDUAL RESULTS MAY VARY.</p>
  </div>
  <div class="disclaimer">These statements have not been evaluated by the Food and Drug Administration. This product is not intended to diagnose, treat, cure, or prevent any disease</div>
  <div class="maker">
    <div class="maker__head">FORMULATED BY &amp; MANUFACTURED<br>EXCLUSIVELY FOR:</div>
    <div class="maker__body">Quillon Health,<br>Millbrook, Ct. 06400 * USA<br>support@ quillonlabs.com</div>
  </div>
  <p class="ingredients"><b>INGREDIENTS:</b> Lorem Ipsum is simply dummy text of the printing and typesetting industry. Lorem Ipsum has been the industry’s standard dummy text ever since the 1500s.</p>
</section>
</body>
</html>
```